dulvox presentation

I would like to improve the presentation of the PoweePoint. That attached.

Target Market(s)

Hotel sector - laboratories - industry

Font styles to use
Other font styles liked:
• como las del diseño

Requirements
Must have
• This PowerPoint. it has to serve as a company presentation.
Nice to have
• I wish it were pleasant to read. with background images or photographs that reinforce the text.

```html
<!DOCTYPE html>
<html lang="ca">
<head>
<meta charset="utf-8">
<title>dulvox – Presentació dels serveis</title>
<link href="https://fonts.googleapis.com/css2?family=Mulish:wght@400;600;700;800;900&display=swap" rel="stylesheet">
<style>
:root{
  --blue:#1d5aa8;
  --blue-dark:#164a8c;
  --red:#e01f26;
  --ink:#222326;
  --grey-text:#55585e;
  --page:#e6e6e6;
  --rule:#e3e3e3;
  --slate:#3b3d41;
  --caption:#efefef;
}
*{box-sizing:border-box;margin:0;padding:0}
html,body{width:1200px;height:4839px;overflow:hidden}
body{background:var(--page);font-family:"Mulish",sans-serif;color:var(--ink);position:relative}
.slide{position:absolute;left:45px;width:1110px;background:#fff;overflow:hidden}
.abs{position:absolute}
.photo{position:absolute}
.brand{font-family:"Mulish",sans-serif;font-weight:800;letter-spacing:1px;text-transform:uppercase}
.brand-sm{position:absolute;left:30px;top:22px;font-size:34px;color:var(--blue)}
.head-caption{position:absolute;right:36px;top:34px;font-size:12px;font-weight:600;letter-spacing:.3px;color:var(--ink)}
.head-caption .accent{color:var(--red);font-weight:800}
.head-rule{position:absolute;left:0;right:0;top:80px;height:1px;background:var(--rule)}
.cover{top:66px;height:742px}
.cover .brand-lg{position:absolute;left:43px;top:605px;font-size:76px;color:var(--blue);line-height:1}
.cover .tagline{position:absolute;left:45px;top:690px;font-size:12.5px;font-weight:800;color:var(--ink);letter-spacing:.2px}
.cover .title{position:absolute;left:650px;top:610px;font-size:36px;font-weight:900}
.cover .url{position:absolute;left:650px;top:662px;font-size:21px;font-weight:800;color:var(--red)}
.dark-slide .brand-sm{color:#fff}
.dark-slide .head-caption{color:#fff}
.dark-slide .head-rule{background:rgba(255,255,255,.35)}
.tile{position:absolute;border:3px solid #fff;height:245px;display:flex;flex-direction:column;align-items:center;padding-top:38px;color:#fff;text-align:center}
.tile .disc{width:76px;height:76px;border-radius:50%;background:var(--red);display:flex;align-items:center;justify-content:center}
.tile .dash{width:54px;height:3px;background:#fff;margin:22px 0 18px}
.tile .label{font-size:20px;font-weight:800;line-height:1.2}
.tile .label.light{font-weight:600}
.intro-line{position:absolute;left:0;right:0;text-align:center;font-size:26px;font-weight:400}
.intro-line b{font-weight:800}
.intro-line.red{color:var(--red);font-weight:800}
.area-title{position:absolute;left:740px;width:250px;text-align:center;top:290px;font-size:28px;font-weight:400}
.area{position:absolute;width:160px;text-align:center;font-size:13.5px;font-weight:600}
.area .disc{width:88px;height:88px;border-radius:50%;background:var(--red);margin:0 auto 14px;box-shadow:0 3px 6px rgba(0,0,0,.3);display:flex;align-items:center;justify-content:center}
.service-name{font-size:19px;font-weight:900;line-height:1.15;margin-bottom:10px;text-transform:uppercase}
.service-text{font-size:13.5px;line-height:1.4;color:var(--grey-text)}
.svc-left{position:absolute;width:300px;left:62px;text-align:right}
.svc-right{position:absolute;width:300px;left:723px}
.hex{position:absolute;width:132px;height:150px}
.project{position:absolute;background:var(--caption)}
.project .caption{position:absolute;left:0;right:0;bottom:0;height:50px;display:flex;align-items:center;justify-content:center;font-size:17px;font-weight:600}
.project .photo{left:0;top:0;right:0;bottom:50px;border-bottom:3px solid var(--red)}
.thanks-title{position:absolute;left:0;right:0;top:150px;text-align:center;color:#fff;font-size:44px;font-weight:800;letter-spacing:.5px}
.thanks-name{position:absolute;left:0;right:0;top:218px;text-align:center;color:#fff;font-size:22px;font-weight:800;line-height:1.5}
.bottom-stripe{position:absolute;left:0;right:0;bottom:0;height:9px;background:linear-gradient(90deg,var(--red) 0 72%,var(--blue) 72% 100%)}
</style>
</head>
<body>

<section class="slide cover">
  <div class="photo" role="img" aria-label="Fotografia d'un tècnic amb casc blau revisant un quadre elèctric" style="left:0;top:0;width:1110px;height:580px;background:linear-gradient(135deg,#c9ccd2 0%,#8e949c 40%,#5b6068 70%,#3e4349 100%)"></div>
  <svg class="abs" style="left:0;top:470px" width="1110" height="140" viewBox="0 0 1110 140">
    <path d="M0 50 Q520 175 1110 40 L1110 140 L0 140 Z" fill="#fff"/>
    <path d="M0 50 Q520 175 1110 40 L1110 52 Q520 188 0 68 Z" fill="var(--blue)"/>
  </svg>
  <div class="brand brand-lg">dulvox</div>
  <div class="tagline">REALITZEM I CUIDEM LES TEVES INSTAL·LACIONS</div>
  <div class="title">Presentació dels serveis</div>
  <div class="url">www.dulvox.com</div>
</section>

<section class="slide dark-slide" style="top:849px;height:747px;background:var(--blue)">
  <div class="photo" role="img" aria-label="Fotografia en blau d'un tècnic treballant en unitats d'aire condicionat" style="inset:0;background:linear-gradient(120deg,#2a65b0 0%,#1d5aa8 45%,#3a72b8 70%,#1b4f96 100%)"></div>
  <div class="brand brand-sm" style="top:24px">dulvox</div>
  <div class="head-caption" style="top:40px">ÍNDEX</div>
  <div class="head-rule" style="top:90px"></div>

  <div class="tile" style="left:77px;top:146px;width:302px">
    <div class="disc"><svg width="38" height="38" viewBox="0 0 38 38" fill="none" stroke="#fff" stroke-width="2.4"><rect x="9" y="5" width="20" height="28" rx="2"/><path d="M13 13h12M13 19h12M13 25h8"/></svg></div>
    <div class="dash"></div><div class="label">Introducció</div>
  </div>
  <div class="tile" style="left:406px;top:146px;width:302px">
    <div class="disc"><svg width="38" height="38" viewBox="0 0 38 38" fill="none" stroke="#fff" stroke-width="2.4"><rect x="8" y="5" width="22" height="28" rx="2"/><path d="M12 12h14M12 18h14"/><path d="M14 25l4 4 7-7"/></svg></div>
    <div class="dash"></div><div class="label">Les nostres principals<br>àrees d'acció</div>
  </div>
  <div class="tile" style="left:729px;top:146px;width:302px">
    <div class="disc"><svg width="38" height="38" viewBox="0 0 38 38" fill="none" stroke="#fff" stroke-width="2.4"><circle cx="14" cy="14" r="6"/><circle cx="26" cy="24" r="5"/><path d="M8 30l9-9M24 8l6 6"/></svg></div>
    <div class="dash"></div><div class="label">Instal·lacions amb<br>valor afegit</div>
  </div>
  <div class="tile" style="left:201px;top:417px;width:302px">
    <div class="disc"><svg width="38" height="38" viewBox="0 0 38 38" fill="none" stroke="#fff" stroke-width="2.4"><path d="M10 17a9 9 0 0 1 18 0z"/><path d="M8 17h22"/><path d="M9 33c1-7 5-9 10-9s9 2 10 9"/></svg></div>
    <div class="dash"></div><div class="label">Anticipar-se.<br>Solucionar. Mantenir</div>
  </div>
  <div class="tile" style="left:533px;top:417px;width:376px">
    <div class="disc"><svg width="38" height="38" viewBox="0 0 38 38" fill="none" stroke="#fff" stroke-width="2.4"><path d="M5 20l7-7 7 4 7-4 7 7-10 10H15z"/><path d="M19 17l5 5"/></svg></div>
    <div class="dash"></div><div class="label">La satisfacció dels nostres<br>clients és el nostre major aval</div>
  </div>
</section>

<section class="slide" style="top:1638px;height:770px">
  <div class="brand brand-sm">dulvox</div>
  <div class="head-caption">LES NOSTRES PRINCIPALS ÀREES D'ACCIÓ</div>
  <div class="head-rule"></div>
  <div class="intro-line" style="top:132px">A <b>dulvox tenim un leitmotiv que</b> ens acompanya dia rere dia, any rere any:</div>
  <div class="intro-line red" style="top:176px">oferir un servei prèmium per a clients selectes</div>

  <div class="photo" role="img" aria-label="Fotografia del vestíbul d'un hotel" style="left:83px;top:263px;width:308px;height:210px;background:linear-gradient(135deg,#8a7a66,#c7bfb3 55%,#5b5046)"></div>
  <div class="photo" role="img" aria-label="Fotografia d'una habitació d'hotel" style="left:411px;top:267px;width:219px;height:206px;background:linear-gradient(135deg,#6b4c36,#d9cfc4 55%,#9a7a5d)"></div>
  <div class="photo" role="img" aria-label="Fotografia d'unes oficines blanques" style="left:83px;top:491px;width:264px;height:212px;background:linear-gradient(135deg,#dfe3e6,#f4f5f6 50%,#aeb5bb)"></div>
  <div class="photo" role="img" aria-label="Fotografia d'una cambrera preparant cafè en un establiment" style="left:366px;top:491px;width:264px;height:212px;background:linear-gradient(135deg,#e0b93c,#7a6a54 55%,#2f2c2a)"></div>

  <div class="area-title">Àrees d'acció:</div>
  <div class="abs" style="left:864px;top:358px;width:1px;height:310px;background:var(--rule)"></div>
  <div class="abs" style="left:715px;top:521px;width:300px;height:1px;background:var(--rule)"></div>
  <div class="area" style="left:677px;top:376px"><div class="disc"><svg width="44" height="44" viewBox="0 0 44 44" fill="none" stroke="#fff" stroke-width="2.2"><rect x="8" y="12" width="28" height="24"/><path d="M14 18h4M20 18h4M26 18h4M14 24h4M20 24h4M26 24h4M19 36v-6h6v6"/></svg></div>RESTAURANTS</div>
  <div class="area" style="left:891px;top:376px"><div class="disc"><svg width="44" height="44" viewBox="0 0 44 44" fill="none" stroke="#fff" stroke-width="2.2"><path d="M8 22L22 10l14 12"/><path d="M12 20v16h20V20"/><rect x="18" y="26" width="8" height="10"/></svg></div>RESIDÈNCIES</div>
  <div class="area" style="left:677px;top:546px"><div class="disc"><svg width="44" height="44" viewBox="0 0 44 44" fill="none" stroke="#fff" stroke-width="2.2"><rect x="12" y="8" width="20" height="28"/><path d="M16 14h4M24 14h4M16 20h4M24 20h4M16 26h4M24 26h4"/></svg></div>OFICINES</div>
  <div class="area" style="left:891px;top:546px"><div class="disc"><svg width="44" height="44" viewBox="0 0 44 44" fill="none" stroke="#fff" stroke-width="2.2"><path d="M8 16h28l-3-7H11z"/><path d="M10 16v20h24V16"/><rect x="14" y="22" width="7" height="14"/><rect x="24" y="22" width="7" height="6"/></svg></div>COMERÇOS</div>
</section>

<section class="slide" style="top:2455px;height:725px">
  <div class="brand brand-sm">dulvox</div>
  <div class="head-caption">LA SATISFACCIÓ DELS NOSTRES CLIENTS ÉS EL NOSTRE MAJOR AVAL &nbsp;I&nbsp; <span class="accent">SERVEIS</span></div>
  <div class="head-rule"></div>
  <div class="intro-line" style="top:140px;font-size:25px;font-weight:700">A dulvox estem en constant compromís amb la superació.</div>
  <div class="intro-line" style="top:187px;font-size:20px">Aquests són només alguns exemples dels <b style="color:var(--red)">serveis</b> que oferim als nostres clients:</div>

  <svg class="hex" style="left:396px;top:282px" viewBox="0 0 132 150"><polygon points="66,4 127,39 127,111 66,146 5,111 5,39" fill="#fff" stroke="var(--red)" stroke-width="9"/><g fill="none" stroke="var(--blue)" stroke-width="3"><circle cx="66" cy="62" r="12"/><path d="M44 100l14-10 8 6 8-6 14 10"/></g></svg>
  <svg class="hex" style="left:560px;top:282px" viewBox="0 0 132 150"><polygon points="66,4 127,39 127,111 66,146 5,111 5,39" fill="#fff" stroke="var(--red)" stroke-width="9"/><g fill="none" stroke="var(--blue)" stroke-width="3"><rect x="44" y="48" width="44" height="54"/><path d="M52 58h6M62 58h8M74 58h6M52 70h6M62 70h8M74 70h6M52 82h6M62 82h8M74 82h6M60 102V92h12v10"/></g></svg>
  <svg class="hex" style="left:396px;top:452px" viewBox="0 0 132 150"><polygon points="66,4 127,39 127,111 66,146 5,111 5,39" fill="#fff" stroke="var(--red)" stroke-width="9"/><g fill="none" stroke="var(--blue)" stroke-width="3"><path d="M50 70a16 16 0 0 1 32 0z"/><path d="M46 70h40"/><path d="M46 104c2-12 10-16 20-16s18 4 20 16"/></g></svg>
  <svg class="hex" style="left:560px;top:452px" viewBox="0 0 132 150"><polygon points="66,4 127,39 127,111 66,146 5,111 5,39" fill="#fff" stroke="var(--red)" stroke-width="9"/><g fill="none" stroke="var(--blue)" stroke-width="3"><rect x="44" y="50" width="44" height="50" rx="4"/><path d="M54 90l24-30M56 60l22 28"/></g></svg>

  <div class="svc-left" style="top:305px"><div class="service-name">Laboratoris Vertex</div><div class="service-text">Legalització i adaptació de les plantes refredadores. Instal·lació d'unitats UTA a la zona packaging.</div></div>
  <div class="svc-left" style="top:478px"><div class="service-name">Norvia</div><div class="service-text">Manteniment correctiu i<br>preventiu.</div></div>
  <div class="svc-right" style="top:285px"><div class="service-name">Hotel Nord i Hotel<br>Aurora</div><div class="service-text">Canvi de sala de calderes de producció semiinstantània. Estalvi previst: 30 % en electricitat i 35 % en gas, segons el projecte d'eficiència energètica.</div></div>
  <div class="svc-right" style="top:478px"><div class="service-name">Hotel Sant Roc</div><div class="service-text">Canvi de l'antic sistema de calderes amb acumulació per un sistema de producció d'ACS semiinstantani. Fins al moment portem el 38 % d'estalvi en la factura de gas</div></div>
</section>

<section class="slide" style="top:3223px;height:834px">
  <div class="brand brand-sm">dulvox</div>
  <div class="head-caption">LA SATISFACCIÓ DELS NOSTRES CLIENTS ÉS EL NOSTRE MAJOR AVAL &nbsp;I&nbsp; <span class="accent">PROJECTES</span></div>
  <div class="head-rule"></div>
  <div class="intro-line" style="top:134px;font-size:27px;font-weight:600">Alguns dels <b style="color:var(--red)">projectes</b> que hem realitzat a dulvox:</div>

  <div class="project" style="left:58px;top:207px;width:320px;height:270px"><div class="photo" role="img" aria-label="Fotografia nocturna de la façana d'un hotel il·luminat" style="background:linear-gradient(180deg,#1d2545,#6b5a3a 55%,#d8b45c 80%,#2a2a2a)"></div><div class="caption">Hotel Miralls de Barcelona</div></div>
  <div class="project" style="left:395px;top:207px;width:321px;height:270px"><div class="photo" role="img" aria-label="Fotografia d'un celler de restaurant amb taula il·luminada" style="background:linear-gradient(180deg,#2b2b2b,#141414 50%,#cfd8d0 70%,#1a1a1a)"></div><div class="caption">Restaurant Brasa, Barcelona</div></div>
  <div class="project" style="left:732px;top:207px;width:320px;height:270px"><div class="photo" role="img" aria-label="Fotografia d'unes oficines amb mampares de vidre" style="background:linear-gradient(135deg,#c7cbcf,#f2f2f2 50%,#8d9296)"></div><div class="caption">Oficines Grupcor, Barcelona</div></div>
  <div class="project" style="left:58px;top:497px;width:658px;height:270px"><div class="photo" role="img" aria-label="Fotografia de l'interior d'una residència amb cuina blanca" style="background:linear-gradient(90deg,#6e5a4e,#a88f7e 30%,#e9e6e1 55%,#f4f4f4 80%,#cfcfcf)"></div><div class="caption">Residència Els Pins, Barcelona</div></div>
  <div class="project" style="left:732px;top:497px;width:320px;height:270px"><div class="photo" role="img" aria-label="Fotografia de la façana d'una botiga de perfumeria" style="background:linear-gradient(180deg,#111,#3a3a3a 50%,#8a5a6a 75%,#222)"></div><div class="caption">Perfumeria Aroa, Barcelona</div></div>
</section>

<section class="slide dark-slide" style="top:4094px;height:680px;background:var(--slate)">
  <div class="brand brand-sm" style="top:24px">dulvox</div>
  <div class="head-caption" style="top:40px">ÍNDEX</div>
  <div class="thanks-title">MOLTES GRÀCIES</div>
  <div class="thanks-name">Marc Ferrer Soler<br>Enginyer Industrial I CEO</div>

  <div class="tile" style="left:77px;top:329px;width:302px">
    <div class="disc"><svg width="38" height="38" viewBox="0 0 38 38" fill="none" stroke="#fff" stroke-width="2.6"><path d="M11 7l5 6-3 4c2 4 5 7 9 9l4-3 6 5-3 4C18 32 6 20 7 10z"/></svg></div>
    <div class="dash"></div><div class="label">+34 612 345 678</div>
  </div>
  <div class="tile" style="left:406px;top:329px;width:302px">
    <div class="disc"><svg width="38" height="38" viewBox="0 0 38 38" fill="none" stroke="#fff" stroke-width="2.6"><path d="M19 33s-10-10-10-17a10 10 0 0 1 20 0c0 7-10 17-10 17z"/><circle cx="19" cy="16" r="4"/></svg></div>
    <div class="dash"></div><div class="label light">C. de l'Olivera,<br>14, 08017 - Barcelona</div>
  </div>
  <div class="tile" style="left:729px;top:329px;width:302px">
    <div class="disc"><svg width="38" height="38" viewBox="0 0 38 38" fill="none" stroke="#fff" stroke-width="2.4"><circle cx="19" cy="19" r="13"/><ellipse cx="19" cy="19" rx="6" ry="13"/><path d="M6 19h26M8 12h22M8 26h22"/></svg></div>
    <div class="dash"></div><div class="label">www.dulvox.com</div>
  </div>
  <div class="bottom-stripe"></div>
</section>

</body>
</html>
```